Property lawyer needs a website for new law firm Sydney

WHO AM I ?
I am a real estate development lawyer based in suburban Sydney Australia with over 14 years experience and have recently started my own law firm "Tallowbrook Legal". The firm is just me (a female) at this stage. I need a website designed that is capable of being edited by me frequently (hoping this is easily done?!) and can be published with the domain name I own - www.tallowbrooklegal.com.au.
My areas of practice are:
* Property development (strata & community titling, due diligence, easements, by-laws and management statements, structuring etc)
* Conveyancing (sale and purchase of residential, commercial and retail property)
* General property law (caveats, transfers, related party transactions, easements, leases, powers of attorney etc).
WEBSITE REQUIREMENTS
I would like a website which conveys professionalism, has a fresh modern corporate look and is easy to navigate. The website will mostly be accessed by potential clients looking for information about me, my areas of practice and how to get in contact with me. My potential clients are corporate developers and individuals who are buying and selling property.
My logo for Tallowbrook Legal (see attached) is simple, clean and professional looking. I would like the website to work with the logo without being too dark.
I haven't written all of the content yet, so please use filler text for everything and structure the menus as described above. The site will need to be capable of being updated and edited by me.
Other than that I will leave the design up to you.
Thanks and happy designing!
Target Market(s)
Professional developers and individuals buying and selling real estate
Industry/Entity Type
Real Estate
Coding
Coded - Design and coding required
Number of Pages Required
4 page
Requirements
Must have
- I would like a website which conveys professionalism, has a fresh modern corporate look and is easy to navigate. The website will mostly be accessed by potential clients looking for information about me, my areas of practice and how to get in contact with me. My potential clients are corporate developers and individuals who are buying and selling property.
- Please use my logo for Tallowbrook Legal. I would like the website to work with the logo - the colours are a dark blue (C 100% M 50% B 50%) and grey (C10% B 40%). I don't want the website to be too dark though.
- I am thinking 4 pages. I would like links across the top of the page for "Practice Areas", "About us" and "Contact us" - these should lead to separate landing pages with the content to be inserted later.
- The contact page should contain space for a potential client to send an email enquiry to the following email address "enquiries@tallowbrooklegal.com.au". My contact details are set out in the attached letterhead (see attached).
- I would also like the home page to set out what my three Practice Areas are - Property Development; Conveyancing; General Property Law. Each area should have some filler text under it which will be completed later and a link to be able to take me to the "Practice Areas" page where more detail on each will be provided.
- Please select images that are relevant to my practice as a property lawyer. The photos you use will be the ones which I use so please choose wisely.
- I will need a link on the bottom of the home page showing that I am a member of "The Counsel Guild of NSW" (see attached logo).
- The bottom of each page should also include the following statement "Tallowbrook Legal is a business name of Tallowbrook Legal Pty Limited ACN 482 517 306, an incorporated legal practice regulated by the Legal Profession Act 2004. Liability limited by a scheme approved under the Professional Standards Legislation."
Nice to have
- Have attached an image of me (not the best) but at least its me. Consider whether to use on "About us" page
Should not have
- No images of gavels, scales of justice or law books.
- Images not to be too masculine
- Website not to be too dark

```html
<!DOCTYPE html>
<html lang="en">
<head>
<meta charset="utf-8">
<title>Tallowbrook Legal</title>
<link href="https://fonts.googleapis.com/css2?family=Lato:wght@300;400&family=Lora:wght@400&display=swap" rel="stylesheet">
<style>
:root{
  --navy:#003f72;
  --heading:#1d4a78;
  --hex:#3592dc;
  --page:#e8e8e8;
  --label:rgba(214,214,214,.92);
  --label-text:#3f5f80;
  --body:#6f6f6f;
  --nav:#555;
}
*{margin:0;padding:0;box-sizing:border-box}
html,body{width:1200px;height:1157px;overflow:hidden}
body{position:relative;background:var(--page);font-family:'Lato',sans-serif;color:var(--body)}
.site-header{position:absolute;top:0;left:0;width:1200px;height:54px;background:#fff}
.brand{position:absolute;left:299px;top:17px;font-family:'Lora',serif;font-size:13.5px;font-weight:400;letter-spacing:-.4px;text-transform:uppercase;color:var(--navy);white-space:nowrap}
.main-nav{position:absolute;left:532px;top:17px;display:flex;gap:29px;font-size:12px}
.main-nav a{color:var(--nav);text-decoration:none}
.main-nav a.current{color:var(--navy);font-weight:700}
.hero{position:absolute;top:54px;left:0;width:1200px;height:378px;
  background:linear-gradient(180deg,#b9cadb 0%,#7d7f7c 14%,#8a6a4c 30%,#43564a 52%,#33443a 78%,#46573c 100%)}
.hero-band{position:absolute;top:432px;left:0;width:1200px;height:12px;background:var(--navy)}
.section-title{position:absolute;left:0;width:1200px;text-align:center;font-family:'Lora',serif;font-size:27px;font-weight:400;color:var(--heading)}
.practice{position:absolute;top:509px;width:200px}
.practice svg{position:absolute;top:0}
.practice-label{position:absolute;top:47px;height:31px;line-height:31px;background:var(--label);font-size:18px;font-weight:300;color:var(--label-text);text-align:center;white-space:nowrap}
.practice p{position:absolute;top:148px;left:0;font-size:9.6px;line-height:15px;font-weight:300}
.portrait{position:absolute;left:299px;top:848px;width:142px;height:142px;border-radius:50%;
  background:linear-gradient(180deg,#f4f4f4 0%,#e9e2de 45%,#b88f80 75%,#4a3434 100%)}
.about-text{position:absolute;left:459px;top:855px;width:446px;font-size:9.8px;line-height:12px;font-weight:300}
.member-badge{position:absolute;left:797px;top:1010px}
.site-footer{position:absolute;left:0;top:1083px;width:1200px;height:74px;background:var(--navy)}
.footer-card{position:absolute;left:342px;top:1071px;width:517px;height:86px;background:#fff;text-align:center}
.footer-brand{margin-top:17px;font-family:'Lora',serif;font-size:13px;font-weight:400;letter-spacing:-.4px;text-transform:uppercase;color:var(--navy)}
.footer-note{margin:13px auto 0;width:420px;font-size:6.8px;line-height:12px;color:#555}
</style>
</head>
<body>
<header class="site-header">
  <div class="brand">Tallowbrook Legal</div>
  <nav class="main-nav">
    <a href="#" class="current">Home</a>
    <a href="#">Practice Areas</a>
    <a href="#">About Us</a>
    <a href="#">Contact Us</a>
  </nav>
</header>

<div class="hero" role="img" aria-label="Photograph of a suburban two-storey house with timber shingles, green siding and garden"></div>
<div class="hero-band"></div>

<h2 class="section-title" style="top:463px">Practice Areas</h2>

<section class="practice" style="left:299px">
  <svg style="left:45px" width="110" height="124" viewBox="0 0 110 124"><polygon points="55,0 110,31 110,93 55,124 0,93 0,31" fill="var(--hex)"/></svg>
  <div class="practice-label" style="left:0;width:199px">Property Developement</div>
  <p style="width:200px">Lorem ipsum dolor sit amet, consectetur adipiscing elit. Fusce accumsan volutpat venenatis. Suspendisse tincidunt dictum massa quis ullamcorper. Nulla quis est nec orci porttitor dignissim.</p>
</section>

<section class="practice" style="left:511px">
  <svg style="left:41px" width="110" height="124" viewBox="0 0 110 124"><polygon points="55,0 110,31 110,93 55,124 0,93 0,31" fill="var(--hex)"/></svg>
  <div class="practice-label" style="left:0;width:190px">Conveyancing</div>
  <p style="width:182px">Lorem ipsum dolor sit amet, consectetur adipiscing elit. Fusce accumsan volutpat venenatis. Suspendisse tincidunt dictum massa quis ullamcorper. Nulla quis est nec orci porttitor dignissim. Suspendisse leo enim, maximus sit amet fermentum ut, dapibus sed elit. Cras sed finibus magna.</p>
</section>

<section class="practice" style="left:714px">
  <svg style="left:36px" width="110" height="124" viewBox="0 0 110 124"><polygon points="55,0 110,31 110,93 55,124 0,93 0,31" fill="var(--hex)"/></svg>
  <div class="practice-label" style="left:0;width:190px">General Property Laws</div>
  <p style="width:180px">Nulla facilisi. Ut vel est vel diam laoreet fringilla. Quisque eros nunc, vulputate at felis nec, rhoncus tempus quam. Phasellus rhoncus nibh et venenatis venenatis. Quisque nunc dui, pretium in elementum et, hendrerit vitae mauris.</p>
</section>

<h2 class="section-title" style="top:786px">About Us</h2>

<div class="portrait" role="img" aria-label="Portrait photograph of the principal lawyer"></div>
<p class="about-text">Lorem ipsum dolor sit amet, consectetur adipiscing elit. Fusce accumsan volutpat venenatis. Suspendisse tincidunt dictum massa quis ullamcorper. Nulla quis est nec orci porttitor dignissim. Suspendisse leo enim, maximus sit amet fermentum ut, dapibus sed elit. Cras sed finibus magna. Duis sit amet tellus vitae risus varius molestie nec sit amet nibh. Vestibulum congue vulputate augue ac volutpat. Vestibulum ullamcorper nisi quam, nec commodo nibh maximus quis. Vestibulum luctus, orci et vestibulum scelerisque, leo mauris semper ligula, ut ultricies velit mauris quis ante. Aliquam dapibus mauris egestas tellus dapibus ullamcorper vel quis odio. Etiam euismod fringilla augue sed rhoncus. Mauris quis auctor dolor, eget lobortis nisi. Sed cursus libero nibh, nec scelerisque purus mattis a. Ut efficitur viverra massa eu lacinia. Ut aliquet nibh ut nisl volutpat porttitor.</p>

<a class="member-badge" href="#" aria-label="Member of The Counsel Guild of NSW">
  <svg width="108" height="46" viewBox="0 0 108 46"><circle cx="21" cy="23" r="21" fill="#2a2a2a"/><rect x="48" y="11" width="58" height="4" fill="#2a2a2a"/><rect x="48" y="19" width="58" height="3" fill="#2a2a2a"/><rect x="48" y="25" width="58" height="2" fill="#2a2a2a"/></svg>
</a>

<footer class="site-footer"></footer>
<div class="footer-card">
  <div class="footer-brand">Tallowbrook Legal</div>
  <p class="footer-note">Tallowbrook Legal is a business name of Tallowbrook Legal Pty Limited ACN 482 517 306, an incorporated legal practice regulated by the Legal Profession Act 2004. Liability limited by a scheme approved under the Professional Standards Legislation.</p>
</div>
</body>
</html>
```